Webdesign für Versicherungsmakler
Zielgruppe
Wir sind ein Versicherungsmakler und wollen unseren Internetauftritt modernisieren. Unsere Zielgruppe sind mittelständische Unternehmen. Wir erstellen neben den Sachversicherungen und der Altersvororge auch versicherungsmathematische Gutachten. Wir beraten, erstellen Angebote und verwalten und betreuen die Versicherungsverträge und Schadenfälle unserer Kunden.
Aufgabenstellung
Es besteht bereits eine Website: https://www.kl-partner-beispiel.de/. An dieser sollte sich orientiert werden, die Inhalte werden vermutlich in Zukunft Ähnlich bleiben.
Der Aufbau der Website soll modernisiert werden. Das Logo soll erhalten bleiben. Die Seite soll einen modernen, cleanen und dennoch zuverlässigen Eindruck vermitteln.

```html
<!DOCTYPE html>
<html lang="de">
<head>
<meta charset="utf-8">
<title>Keller &amp; Lindner – Versicherungsmakler</title>
<link href="https://fonts.googleapis.com/css2?family=Nunito+Sans:wght@400;600;700;800&display=swap" rel="stylesheet">
<style>
:root{
  --blue:#005b98;
  --blue-dark:#004a7d;
  --orange:#e06b4d;
  --bg:#f5f3f0;
  --white:#ffffff;
  --text:#4a4a4a;
  --grey:#6a6a6a;
  --line:#dcdcdc;
  --photo:#c9c9c9;
}
*{margin:0;padding:0;box-sizing:border-box}
html,body{width:707px;height:1200px;overflow:hidden}
body{background:var(--bg);font-family:"Nunito Sans",sans-serif;color:var(--text);position:relative}
.abs{position:absolute}

/* header */
.brand{left:33px;top:16px;display:flex;align-items:center;gap:7px}
.brand-mark{width:30px;height:29px;background:var(--blue);border-radius:3px}
.brand-name{font-size:13px;line-height:14px;color:var(--grey);letter-spacing:1px;border-left:1px solid var(--grey);padding-left:7px}
.nav{top:23px;left:228px;display:flex;gap:0;font-size:10.5px;color:var(--blue)}
.nav a{position:absolute;white-space:nowrap;color:var(--blue);text-decoration:none}
.nav a.active{color:var(--orange)}
.btn{background:var(--blue);color:var(--white);font-size:9px;font-weight:600;letter-spacing:.8px;display:flex;align-items:center;justify-content:center;border-radius:3px;width:71px;height:20px}

/* hero */
.hero-title{left:33px;top:96px;font-size:20.5px;color:var(--blue);font-weight:400}
.hero-sub{left:40px;top:122px;font-size:24px;color:var(--blue);font-weight:800}
.hero-text{left:39px;top:157px;width:240px;font-size:8px;line-height:14.3px;color:var(--text)}
.glow{left:410px;top:14px;width:314px;height:314px;border-radius:50%;background:radial-gradient(circle,rgba(232,150,130,.55) 0%,rgba(240,190,175,.3) 45%,rgba(245,243,240,0) 70%)}
.hero-photo{left:491px;top:93px;width:158px;height:158px;border:3px solid var(--white);border-top-left-radius:28px;background:linear-gradient(160deg,#6f8fb3 0%,#b9cbe0 45%,#dfe6ee 75%,#9fb2c6 100%)}
.badge{left:438px;top:211px;width:120px;height:30px;background:var(--white);border-radius:3px;box-shadow:0 2px 6px rgba(0,0,0,.08);display:flex;align-items:center;gap:5px;padding-left:7px}
.badge span{font-size:7.6px;color:var(--blue);font-weight:600;line-height:10.5px;text-align:center}
.slider{left:608px;top:294px}

/* welcome */
.center{left:0;width:707px;text-align:center}
.welcome-title{top:320px;font-size:10.8px;font-weight:800;color:var(--blue)}
.welcome-text{top:342px;font-size:5.3px;line-height:11px;color:var(--text)}
.card{top:375px;width:182px;height:157px;background:var(--white);border:1px solid var(--line);border-radius:3px}
.card-art{position:absolute;left:41px;top:28px;width:100px;height:78px;border-radius:4px;background:linear-gradient(135deg,#d8e4ef 0%,#eef3f7 60%,#f4d9cf 100%)}
.card-title{position:absolute;left:0;width:100%;top:116px;text-align:center;font-size:10px;color:var(--blue);font-weight:600;line-height:13.5px}

/* why band */
.band{left:0;top:575px;width:707px;height:258px;background:var(--blue)}
.band-mark{left:126px;top:635px;width:94px;height:90px;background:var(--white);border-radius:4px}
.band-name{left:126px;top:737px;font-size:15px;line-height:15.5px;color:var(--white);letter-spacing:1.2px}
.why-title{left:365px;top:603px;font-size:10.5px;color:var(--white)}
.why-text{left:365px;top:627px;width:262px;font-size:5.3px;line-height:7.4px;color:var(--white)}
.why-text p{margin-bottom:7.3px}
.why-quote{left:365px;top:763px;width:290px;font-size:11px;line-height:15px;font-weight:700;color:var(--white)}

/* team */
.eyebrow{top:875px;font-size:5.3px;color:var(--orange);letter-spacing:.2px}
.team-title{top:884px;font-size:11.5px;font-weight:800;color:var(--blue)}
.team-text{top:902px;font-size:5.3px;line-height:7.4px;color:var(--text)}
.member{top:954px;width:128px;text-align:center}
.photo{width:102px;height:102px;border-radius:50%;margin:0 auto;background:linear-gradient(180deg,#d4d4d4 0%,#bdbdbd 100%)}
.photo.light{background:linear-gradient(180deg,#f1f1f1 0%,#e3e3e3 100%)}
.member-name{margin-top:9px;font-size:12.3px;color:var(--blue);line-height:14px}
.member-role{font-size:8px;color:var(--text);line-height:12px}
.social{display:flex;justify-content:center;gap:3px;margin-top:3px}
.social i{width:12px;height:12px;border-radius:50%;background:var(--blue);display:block}
.team-next{left:626px;top:1000px;width:20px;height:20px;border-radius:50%;background:var(--white);box-shadow:0 1px 4px rgba(0,0,0,.08);display:flex;align-items:center;justify-content:center}
</style>
</head>
<body>

<header>
  <div class="abs brand">
    <div class="brand-mark"></div>
    <div class="brand-name">KELLER<br>&amp; LINDNER</div>
  </div>
  <nav class="abs nav">
    <a class="active" style="left:0">Home</a>
    <a style="left:48px">Profil</a>
    <a style="left:91px">Dienstleistungen</a>
    <a style="left:191px">Unternehmen</a>
    <a style="left:275px">Service</a>
  </nav>
  <div class="abs btn" style="left:577px;top:21px">Kontakt</div>
</header>

<section class="hero">
  <h1 class="abs hero-title">Versicherungsmakler</h1>
  <div class="abs hero-sub">für Unternehmen</div>
  <p class="abs hero-text">is simply dummy text of the printing and typesetting industry. Lorem Ipsum has been the industry’s standard dummy text ever since the 1500s, when an unknown printer took a galley of type and scrambled it to make a type specimen book. It has survived not only five centuries, but also the leap into electronic</p>
  <div class="abs btn" style="left:39px;top:236px">Kontakt</div>

  <div class="abs glow"></div>
  <div class="abs hero-photo" role="img" aria-label="Foto eines modernen, geschwungenen Bürohochhauses mit Glasfassade vor blauem Himmel"></div>
  <div class="abs badge">
    <svg width="16" height="18" viewBox="0 0 16 18"><path d="M8 1 L15 3.5 V8.5 C15 13 11.5 15.8 8 17 C4.5 15.8 1 13 1 8.5 V3.5 Z" fill="none" stroke="#e06b4d" stroke-width="1.4"/></svg>
    <span>Versicherungsmakler<br>für Unternehmen</span>
  </div>
  <svg class="abs slider" width="44" height="14" viewBox="0 0 44 14">
    <path d="M8 1 L2 7 L8 13" fill="none" stroke="#005b98" stroke-width="1.8"/>
    <circle cx="14.5" cy="7" r="2.3" fill="#005b98"/>
    <circle cx="22" cy="7" r="2.3" fill="#cfdbe6"/>
    <circle cx="29.5" cy="7" r="2.3" fill="#cfdbe6"/>
    <path d="M36 1 L42 7 L36 13" fill="none" stroke="#005b98" stroke-width="1.8"/>
  </svg>
</section>

<section class="welcome">
  <h2 class="abs center welcome-title">Willkommen bei Keller &amp; Lindner</h2>
  <p class="abs center welcome-text">Experten für Ihr Versicherungsmanagement und betriebliche Altersversorgung<br>unabhängiger Versicherungsmakler</p>

  <div class="abs card" style="left:75px">
    <div class="card-art" role="img" aria-label="Illustration: Lupe mit Zahnrad, Schutzschild mit Schirm und Kalender"></div>
    <div class="card-title">Versicherungsmanagement</div>
  </div>
  <div class="abs card" style="left:269px">
    <div class="card-art" role="img" aria-label="Illustration: Checkliste mit Schirmsymbol und älterer Person mit Gehstock"></div>
    <div class="card-title">Altersvorsorge</div>
  </div>
  <div class="abs card" style="left:463px">
    <div class="card-art" role="img" aria-label="Illustration: Schutzschild, Geldkarte und steigendes Balkendiagramm mit Pfeil"></div>
    <div class="card-title" style="text-align:left;padding-left:30px">Versicherungsmathematische<br>&nbsp;Gutachten</div>
  </div>
</section>

<section>
  <div class="abs band"></div>
  <div class="abs band-mark"></div>
  <div class="abs band-name">KELLER<br>&amp; LINDNER</div>
  <h2 class="abs why-title" style="font-weight:400">Warum Keller und Lindner?</h2>
  <div class="abs why-text">
    <p>Wir sind Ihr Partner, um Ihren Visionen, ob als Unternehmer oder Privatperson, nachhaltig Sicherheit zu geben.</p>
    <p>Sie haben Verantwortung für Ihr Unternehmen und wissen, es gibt Risiken, die Ihre Kunden, Ihre Mitarbeiter und Sie gefährden. Ein kluges Risikomanagement ist erforderlich.</p>
    <p>Ein Teil dieses Risikomanagements ist die Absicherung durch ein gut konzeptioniertes Versicherungspaket. Nur dafür schon den Überblick zu behalten, erfordert Sachverstand, Markt- und Branchenkenntnis. Die notwendige Zeit dafür haben Sie wahrscheinlich nicht.</p>
    <p>Mit versicherungsmathematischem Sachverstand übernehmen wir unabhängig von Versicherungsgesellschaften Ihr Versicherungs- und Vorsorgemanagement. Dabei können Sie auf unsere langjährige Erfahrung setzen.</p>
    <p>Der Service macht den Unterschied. Wir wollen, dass Sie sich zu jederzeit bei uns gut aufgehoben fühlen. Neben der Beratung zählt auch die Zuverlässigkeit und Hilfe im Schadenfall. Dabei ist es unser Ziel, zur Zufriedenheit unserer Mandanten zu handeln.</p>
  </div>
  <blockquote class="abs why-quote">„Unser Qualitätsanspruch ist Ihre Sicherheit - seit mehr als einem Vierteljahrhundert“</blockquote>
</section>

<section class="team">
  <div class="abs center eyebrow">OUR TEAM</div>
  <h2 class="abs center team-title">Meet the Team</h2>
  <p class="abs center team-text">Vestibulum sollicitudin nunc in eros a justo facilisis rutrum. Aenean id ullamcorper libero.<br>Vestibulum imperdiet nibh tortor mauris</p>

  <svg class="abs" style="left:70px;top:1006px" width="8" height="8" viewBox="0 0 8 8"><path d="M7 4 H1 M3.5 1.5 L1 4 L3.5 6.5" fill="none" stroke="#005b98" stroke-width="1"/></svg>

  <div class="abs member" style="left:102px">
    <div class="photo" role="img" aria-label="Porträtfoto von Thomas Keller"></div>
    <div class="member-name">Thomas Keller</div>
    <div class="member-role">Geschäftsführer</div>
    <div class="social"><i></i><i></i><i></i></div>
  </div>
  <div class="abs member" style="left:230px">
    <div class="photo" role="img" aria-label="Porträtfoto von Bernd Lindner"></div>
    <div class="member-name">Bernd Lindner</div>
    <div class="member-role">Geschäftsführung</div>
    <div class="social"><i></i><i></i><i></i></div>
  </div>
  <div class="abs member" style="left:357px">
    <div class="photo light" role="img" aria-label="Porträtfoto von Sabine Roth"></div>
    <div class="member-name">Sabine Roth</div>
    <div class="member-role">Gutachterin</div>
    <div class="social"><i></i><i></i><i></i></div>
  </div>
  <div class="abs member" style="left:485px">
    <div class="photo light" role="img" aria-label="Porträtfoto von Dr. Klaus Weber"></div>
    <div class="member-name">Dr. Klaus Weber</div>
    <div class="member-role">Berater</div>
    <div class="social"><i></i><i></i><i></i></div>
  </div>

  <div class="abs team-next">
    <svg width="8" height="8" viewBox="0 0 8 8"><path d="M1 4 H7 M4.5 1.5 L7 4 L4.5 6.5" fill="none" stroke="#005b98" stroke-width="1"/></svg>
  </div>
</section>

</body>
</html>
```